Business Card Upgrade

I have designed our business card using our new logo. I think it needs imporovements. We used to have two cards for our business. One card was for our software business, and the other was for our consulting business. We are now in the process of combining our websites, marketing, name, and a new logo.

Our goal is to have a really sharp professional logo. One reason I designed the card the way I did was that our Titles are sometimes long, and by separating the person's name and title, it shows up very well and the title can be adjusted no matter how long it is. Sometimes the title can be 4 or 5 words or more.

We really like our logo on black as it shows up very nice. Our PMS colors are as follows: 368C and 459C.

The Designer that will be working with us will need to deliver the following:

The front and back of the Business Card Design will need to be delivered in a high quality JPEG, and
The front and back of the Business Card Design in Illustrator Format .ai
Any fonts will need to be sent to us if they are not standard and are required to open the Illustrator file correctly.

To help us get a good idea of the card with a title, please use the title: " Director of Software Development "

NOTE: The chosen designer will be selected to design our new letterhead within 2 weeks from the closing of this contest.

To help us make sure the card design works with longer titles, please use the followign job title on the card:  

"Director of Software and Product Development"

 

ALL DESIGNERS:

1. I appreciate the different angles you are showing the cards, but please be sure and always show the direct view, so I can see the layout and what the person I hand the card will see.

2. Please do not use white.  Please use off white as I don't care for white cards and they get dirty easy and do not represent the designs well.

Dear Designers,

Please provide samples straight one as a viewer of the card will see.  Some of the angles that are presented make it impossible to tell how everything fits, and sometimes even makes areas look skewed. So, please provide a straight sample view.

Pinnacle 400 company executives such as Vice Presidents, and Directors

Software

• Professional looking Card.

Our customers are Directors, Vice Presidents, and Presidents of companies as large as Pinnacle 400 companies. The card needs to get attention wile still looking professional.

Delivery of the finished product in Illustrator Format with any fonts needed to edit the text or open the file.

The card will be a heavy stock with a soft touch coating for that silk feel.

```html
<!DOCTYPE html>
<html lang="en">
<head>
<meta charset="utf-8">
<title>Meridian Port Commerce – Business Card, Front and Back</title>
<link rel="stylesheet" href="https://fonts.googleapis.com/css2?family=Poppins:wght@300;400;500&family=Raleway:wght@200&display=swap">
<style>
  :root {
    --backdrop: #1e5446;
    --card-stock: #fbfaf5;
    --ink: #111111;
    --panel-black: #0c0c0c;
    --brand-green: #2bb673;
    --brand-gold: #d8c98a;
    --card-shadow: rgba(0, 0, 0, 0.35);
  }
  * { margin: 0; padding: 0; box-sizing: border-box; }
  html, body {
    width: 1200px;
    height: 1200px;
    overflow: hidden;
    background: var(--backdrop);
  }
  .canvas {
    position: relative;
    width: 1200px;
    height: 1200px;
  }
  .card {
    position: absolute;
    left: 180px;
    width: 840px;
    height: 480px;
    background: var(--card-stock);
    box-shadow: 0 14px 40px var(--card-shadow);
    overflow: hidden;
  }
  .card--front { top: 90px; }
  .card--back  { top: 630px; }

  /* Front */
  .brand-panel {
    position: absolute;
    left: 220px;
    top: 0;
    width: 340px;
    height: 220px;
  }
  .brand-panel svg { display: block; }
  .brand-name {
    position: absolute;
    left: 0;
    top: 58px;
    width: 340px;
    display: flex;
    align-items: center;
    justify-content: center;
    gap: 16px;
  }
  .brand-name__dot {
    width: 22px;
    height: 22px;
    border-radius: 50%;
    background: var(--brand-green);
    flex: none;
  }
  .brand-name__text {
    font-family: "Poppins", sans-serif;
    font-weight: 400;
    font-size: 27px;
    line-height: 1.25;
    color: var(--card-stock);
  }

  .person {
    position: absolute;
    right: 400px;
    top: 272px;
    text-align: right;
    font-family: "Poppins", sans-serif;
    color: var(--ink);
  }
  .person__name { font-size: 31px; font-weight: 500; margin-bottom: 12px; }
  .person__title { font-size: 22px; font-weight: 300; line-height: 1.35; }

  .contact {
    position: absolute;
    left: 470px;
    top: 256px;
    font-family: "Poppins", sans-serif;
    font-weight: 300;
    font-size: 21px;
    line-height: 1.6;
    color: var(--ink);
    list-style: none;
  }

  /* Back */
  .back-art { position: absolute; inset: 0; }
  .web-address {
    position: absolute;
    left: 60px;
    top: 160px;
    font-family: "Raleway", sans-serif;
    font-weight: 200;
    font-size: 62px;
    letter-spacing: 1px;
    color: var(--brand-gold);
  }
  .web-address__name { color: var(--brand-green); }
</style>
</head>
<body>
<main class="canvas">

  <section class="card card--front" aria-label="Business card front">
    <div class="brand-panel">
      <svg width="340" height="220" viewBox="0 0 340 220" aria-hidden="true">
        <path d="M0 0 H340 V170 C260 150 160 215 0 200 Z" fill="var(--panel-black)"/>
        <path d="M0 200 C160 215 260 150 340 170" fill="none" stroke="var(--brand-gold)" stroke-width="5"/>
      </svg>
      <p class="brand-name">
        <span class="brand-name__dot" aria-hidden="true"></span>
        <span class="brand-name__text">Meridian Port<br>Commerce</span>
      </p>
    </div>

    <div class="person">
      <h1 class="person__name">Daniel Marsh</h1>
      <p class="person__title">Director of Software and<br>Product Development</p>
    </div>

    <ul class="contact">
      <li>418 Cedar Bend Lane</li>
      <li>Fairhope, AL 36532</li>
      <li>555.203.4817 (Direct)</li>
      <li>dmarsh@meridianport.com</li>
    </ul>
  </section>

  <section class="card card--back" aria-label="Business card back">
    <svg class="back-art" width="840" height="480" viewBox="0 0 840 480" aria-hidden="true">
      <path d="M0 0 H840 V170 C700 190 560 330 330 480 H0 Z" fill="var(--panel-black)"/>
      <path d="M840 178 C700 198 565 338 345 480" fill="none" stroke="var(--brand-gold)" stroke-width="8"/>
    </svg>
    <p class="web-address">www.<span class="web-address__name">meridianport</span>.com</p>
  </section>

</main>
</body>
</html>
```